Pizzakarton designen
Sehr angenehmer Kontakt ! Vorschläge wurde prompt umgesetzt - sogar am Wochenende ! So wünscht man sich einen Grafiker
Zielgruppe
Wir sind ein Hotel im höchsten Skigebiet Österreichs (Kühtai) - weiters haben wir eine Pizzeria im Haus und planen ab kommendem Winter auch Pizza auszuliefern - dazu benötigen wir coole Pizza-Kartons - diese sollten von Ihnen gestaltet werden.
Die Seitenlaschen der Pizza-Kartons werden von einem örtlichen Sportgeschäft (Alpinsport Brunnauer) als Werbefläche 'gekauft'. Dessen Homepage ist: www.brettmiete.at
ZUSATZ: Die Pizza-Kartons werden im Digitaldruck erstellt - man kann sich also mit den Farben ruhig 'austoben'
Diese Firma wird die Kartons erstellen - da sieht man Beispiele:
https://www.tellerbox-druck.de/de/
Unsere eigene Homepage vom Hotel ist: www.almgrund-hotel.at
In einem weiteren Schritt würden wir evtl. auch Flyer benötigen. Diese sollten dann natürlich das Design der Pizzakartons wiederspiegeln.
Letztes Jahr hatten wir Flyer wie unter: www.tonis.pizza zu sehen.
Da diese aber fast zu klein waren, würden wir dieses Jahr auf Flyer mit Z-Falz setzen
Bei den Dateien ist einerseits die Druckvorlage des Pizza-Kartons und das Logo der Pizzeria - farblich kann das Logo natürlich geändert werden.
Hab noch ein fertiges Karton-Design dazugefügt - dies dient aber lediglich dazu, damit man weiß wie die Ausrichtung sein muss, damit am Schluss nicht alles Kopf steht (im übrigen - dieses Design gefällt mir nicht wirklich )
Aufgabenstellung
Es gibt eigentlich keine genauen Vorgaben - der Gesamt-Eindruck muss einfach stimmen

```html
<!DOCTYPE html>
<html lang="de">
<head>
<meta charset="UTF-8">
<title>Pizzakarton – Toni's Restaurant</title>
<link rel="stylesheet" href="https://fonts.googleapis.com/css2?family=Open+Sans:wght@400;600&family=Allura&display=swap">
<style>
  :root {
    --page-bg: #f2f0ed;
    --wood-light: #c7793f;
    --wood-mid: #a85a2a;
    --wood-dark: #7a3e1c;
    --plank-line: rgba(60, 28, 10, 0.55);
    --logo-box: #5b4b3f;
    --logo-gold: #c9a46a;
    --band-red: #9b1c1f;
    --text-light: #fbf3e8;
    --pizza-crust: #d9a464;
    --pizza-red: #b8341f;
  }
  * { margin: 0; padding: 0; box-sizing: border-box; }
  html, body {
    width: 1200px; height: 803px; overflow: hidden;
    background: var(--page-bg);
    font-family: "Open Sans", sans-serif;
  }
  .box-artwork {
    position: absolute; left: 290px; top: 24px;
    width: 620px; height: 755px;
  }
  .lid {
    position: relative; width: 620px; height: 620px; overflow: hidden;
    background: linear-gradient(160deg, var(--wood-light) 0%, var(--wood-mid) 55%, var(--wood-dark) 100%);
  }
  .lid-planks, .flap-planks { position: absolute; inset: 0; }
  .logo-plate {
    position: absolute; left: 150px; top: 0; width: 210px; height: 150px;
    background: var(--logo-box);
    display: flex; align-items: center; justify-content: center; gap: 10px;
  }
  .logo-plate .logo-dot { width: 12px; height: 12px; border-radius: 50%; background: var(--logo-gold); }
  .logo-plate .logo-name { color: var(--logo-gold); font-size: 30px; font-weight: 400; letter-spacing: 1px; }
  .slogan {
    position: absolute; left: 110px; top: 300px;
    transform: rotate(-28deg); transform-origin: left top;
    font-family: "Allura", cursive; color: var(--text-light);
    font-size: 34px; line-height: 40px; white-space: nowrap;
  }
  .slogan span { display: block; }
  .slogan .line-2 { padding-left: 70px; }
  .slogan .line-3 { padding-left: 140px; }
  .hotel-pill {
    position: absolute; right: -14px; top: 262px;
    transform: rotate(-28deg);
    background: var(--band-red); color: var(--text-light);
    font-size: 20px; padding: 8px 26px; border-radius: 22px;
    white-space: nowrap;
  }
  .pizza-photo { position: absolute; left: 70px; top: 380px; width: 480px; height: 240px; }
  .flap {
    position: relative; margin-top: 20px; width: 620px; height: 115px; overflow: hidden;
    background: linear-gradient(180deg, var(--wood-mid) 0%, var(--wood-dark) 100%);
    display: flex; align-items: center; justify-content: space-between; padding: 0 30px;
  }
  .sponsor-pill {
    position: relative;
    background: var(--band-red); color: var(--text-light);
    font-size: 21px; padding: 10px 30px; border-radius: 24px;
    white-space: nowrap;
  }
</style>
</head>
<body>
  <main class="box-artwork">
    <section class="lid">
      <svg class="lid-planks" width="620" height="620" role="img" aria-label="Holzdielen-Hintergrund in warmen Brauntönen">
        <g stroke="var(--plank-line)" stroke-width="3">
          <line x1="0" y1="95" x2="620" y2="95"/>
          <line x1="0" y1="210" x2="620" y2="210"/>
          <line x1="0" y1="330" x2="620" y2="330"/>
          <line x1="0" y1="450" x2="620" y2="450"/>
          <line x1="0" y1="565" x2="620" y2="565"/>
        </g>
      </svg>
      <div class="logo-plate"><span class="logo-dot"></span><span class="logo-name">TONI'S</span></div>
      <p class="slogan">
        <span class="line-1">Frische hausgemachte</span>
        <span class="line-2">Pizza nach original</span>
        <span class="line-3">neapolitanischer Rezeptur</span>
      </p>
      <div class="hotel-pill">www.almgrund-hotel.at</div>
      <svg class="pizza-photo" width="480" height="240" role="img" aria-label="Foto einer Pizza mit Tomaten, Mozzarella, Basilikum, Oliven und Salami">
        <defs>
          <radialGradient id="pizzaTone" cx="50%" cy="100%" r="100%">
            <stop offset="0%" stop-color="var(--pizza-red)"/>
            <stop offset="55%" stop-color="var(--pizza-crust)"/>
            <stop offset="100%" stop-color="#b07a3e"/>
          </radialGradient>
        </defs>
        <path d="M0 240 A240 240 0 0 1 480 240 Z" fill="url(#pizzaTone)"/>
      </svg>
    </section>
    <section class="flap">
      <svg class="flap-planks" width="620" height="115" aria-hidden="true">
        <g stroke="var(--plank-line)" stroke-width="3">
          <line x1="90" y1="0" x2="90" y2="115"/>
          <line x1="200" y1="0" x2="200" y2="115"/>
          <line x1="310" y1="0" x2="310" y2="115"/>
          <line x1="420" y1="0" x2="420" y2="115"/>
          <line x1="530" y1="0" x2="530" y2="115"/>
        </g>
      </svg>
      <div class="sponsor-pill">www.brettmiete.at</div>
      <div class="sponsor-pill">www.brettmiete.at</div>
    </section>
  </main>
</body>
</html>
```